Website for IT technology distribution company

Small business distributor of remote IT/Telecoms technology services in Canada

Looking for a bold, clean and professional design for WordPress. We would like a web site design from a designer who may be able to help us upload the site to WordPress (Ideally CSS files).
The website will have the following pages:
1) Home
2) Register
3) Packages
4) Contact

I am also attaching the company logo (with sourcefile, images for page 1 and details on wording/content for website)

Design must use colors that compliment the logo

Must Have:
- Must contain the logo in the header

Should Not Have:
- must not be blog or magazine style layout or look and feel

Industry/Entity Type

Business

```html
<!DOCTYPE html>
<html lang="en">
<head>
<meta charset="utf-8">
<title>Norvale Solutions</title>
<link rel="stylesheet" href="https://fonts.googleapis.com/css2?family=Arvo&family=Oswald&family=Open+Sans&display=swap">
<style>
:root{
  --red:#ee3338;
  --slate:#6b7590;
  --heading-slate:#6f7585;
  --ink:#222;
  --link:#1f3f9a;
  --white:#fff;
  --rule:#d9d9d9;
}
*{box-sizing:border-box;margin:0;padding:0}
html,body{width:1083px;height:1200px;overflow:hidden;background:var(--white)}
body{position:relative;font-family:"Open Sans",Arial,sans-serif;color:var(--ink)}
.page-edge{position:absolute;left:0;top:186px;width:3px;height:954px;background:var(--rule)}
.brand{position:absolute;left:29px;top:30px;display:flex;align-items:center;gap:14px}
.brand-mark{width:22px;height:22px;background:var(--red)}
.brand-name{font-family:"Arvo",serif;font-size:40px;color:var(--slate);letter-spacing:1px}
.contact-info{position:absolute;right:21px;top:28px;text-align:right;font-family:Arial,sans-serif;font-size:17px;color:var(--ink);line-height:29px}
.contact-info div{display:flex;align-items:center;justify-content:flex-end;gap:6px}
.site-nav{position:absolute;left:3px;top:130px;width:1080px;height:56px;background:var(--slate);display:flex;border-bottom:2px solid var(--rule)}
.site-nav a{font-family:"Oswald",sans-serif;font-size:21px;color:#111;text-decoration:none;padding:0 16px;line-height:56px}
.site-nav a.current{background:var(--white);color:var(--red)}
.hero{position:absolute;left:25px;top:214px;width:1037px;height:405px;background:radial-gradient(circle at 52% 35%,#d8262c 0,#c9474c 14%,#e9b9bc 32%,#f3dfe0 55%,#e07c82 100%)}
.hero-caption{position:absolute;left:0;bottom:0;width:100%;height:43px;background:rgba(40,40,40,.82);color:#f2f2f2;font-family:Arial,sans-serif;font-size:17px;line-height:43px;padding-left:11px}
h2{font-family:"Arvo",serif;font-weight:400;color:var(--red);font-size:29px}
.welcome{position:absolute;left:25px;top:694px;width:675px}
.welcome p{font-size:15px;line-height:28px;margin:0}
.welcome h2{margin-bottom:22px}
.news{position:absolute;left:729px;top:694px;width:333px}
.news h2{margin-bottom:14px}
.news h3{font-family:"Arvo",serif;font-weight:400;color:var(--heading-slate);font-size:21px;line-height:30px}
.news time{display:block;font-size:13px;line-height:20px;margin-bottom:16px}
.news p{font-size:15px;line-height:28px;margin-bottom:22px}
.news a{color:var(--link);text-decoration:none}
.site-footer{position:absolute;left:3px;top:1139px;width:1080px;height:61px;background:var(--red);border-top:3px solid var(--rule);color:#fde;text-align:center;font-size:15px;line-height:58px}
</style>
</head>
<body>
<div class="page-edge"></div>
<header>
  <div class="brand"><span class="brand-mark"></span><span class="brand-name">Norvale Solutions Ltd</span></div>
  <div class="contact-info">
    <div><svg width="22" height="16" viewBox="0 0 22 16"><rect width="22" height="16" rx="2" fill="#222"/><path d="M1 2l10 8 10-8" stroke="#fff" stroke-width="1.6" fill="none"/></svg>info@norvale.ca</div>
    <div><svg width="19" height="19" viewBox="0 0 19 19"><rect width="19" height="19" rx="3" fill="#222"/><path d="M5 4c1-1 2 0 3 2s0 2-1 3c1 2 2 3 3 3 1-1 1-2 3-1s3 2 2 3c-1 2-4 2-7-1S3 5 5 4z" fill="#fff"/></svg>1-555-010-2740</div>
  </div>
</header>
<nav class="site-nav">
  <a class="current" href="#">Home</a><a href="#">Register</a><a href="#">Packages</a><a href="#">Contact</a>
</nav>
<section class="hero" role="img" aria-label="Laptops connected by cables to a red globe with world map, on a pink digital background">
  <div class="hero-caption">We guarantee immediate, efficient service, anywhere in the world</div>
</section>
<main class="welcome">
  <h2>Welcome to Norvale Solutions</h2>
  <p>Imagine immediate access to highly trained Corviq engineers, without the cost and expense of paying them for a site visit.</p>
  <p>NORVALE is a Canadian based consulting and distributor of Remote Corviq technical services.</p>
  <p>Are you or your customer's network running slow; is there a switch or WLAN issue that needs looking at? Need to deploy a PBX with tight deadlines or when your resource scheduling doesn't allow?</p>
  <p>A remote Corviq expertise is the answer! Cost efficient, fast and you won't be paying for travel times and lunch breaks.</p>
  <p>NORVALE is the sole distributor of Tavrote remote services in Canada. Tavrote is a UK based leader in providing remote technical services.</p>
  <p>A remote Corviq engineer is better for your budget and ICT infrastructure. Efficient network optimization ensures you are getting the most out of your Corviq network technology, ensuring your communications are always up to date, and up to speed.</p>
</main>
<aside class="news">
  <h2>Featured News</h2>
  <article>
    <h3>Remote Network Optimisation</h3>
    <time>March 16, 2014</time>
    <p>Tavrote is a Corviq remote network optimisation service. We provide remote Corviq engineers for more … <a href="#">[Read More...]</a></p>
  </article>
  <article>
    <h3>Corviq Application Support</h3>
    <time>March 15, 2014</time>
    <p>Software Application Support (SAS), Software Application Support plus Upgrades (SASU), and Unified … <a href="#">[Read More...]</a></p>
  </article>
</aside>
<footer class="site-footer">© 2014 - Norvale Solutions ·</footer>
</body>
</html>
```